Veltrano Energy Business Card Design

website: www.veltranoenergy.example
Project: Business Card Design for Veltrano Energy
Name: Dorian Kettle
Title: Founder / Operations Strategist
Visual Identity & Logo:
Logo File: VEL-Logo-FullGradient-Final.png (Attached).
Color Palette: The brand relies on a distinctive Cyan (Blue) to Lime Green gradient.
Background Preference: We want a Dark Mode aesthetic (Deep Matte Black, Charcoal, or Dark Slate) to make the neon gradient of the logo pop. This feels more "tech/industrial" than a standard white card.
Design Aesthetic (The "Ops" Vibe):
Concept: "Grid & Infrastructure." We are a solar rental company, focusing on logistics and access.
Typography: White, bold sans-serif text for contact info. High contrast against the dark background.
Accents: Use the Cyan or Lime Green from the logo for thin divider lines or edge painting.
Avoid: No orange/gold (clashes with logo). No cartoon leaves.
Layout Requirements:
Front: Large, centered logo. Maybe a subtle UV gloss spot varnish over the logo icon.
Back: Name, Title, Contact Info.
Texture: Matte finish cardstock with gloss elements.
sample mock up of information on card: https://brivomarkco-my.filehost.example/:i:/g/personal/dorian_kettle_veltranoenergy_example/AbCdEfGhIjKlMnOpQrStUvWxYz012345678?e=Xy12Ab
Logo: https://brivomarkco.filehost.example/:i:/s/VeltranoEnergy/ZyXwVuTsRqPoNmLkJiHgFeDcBa9876543210?e=Pq34Cd

```html
<!DOCTYPE html>
<html lang="en">
<head>
<meta charset="utf-8">
<title>Veltrano Energy Business Card</title>
<link href="https://fonts.googleapis.com/css2?family=Poppins:wght@400;500;600;700&display=swap" rel="stylesheet">
<style>
  :root{
    --navy:#0f2147;
    --navy-soft:#15305a;
    --navy-panel:#123056;
    --cyan:#29b6c8;
    --teal:#35c0b4;
    --lime:#a6d638;
    --white:#ffffff;
    --stage:#e6e8ec;
    --flag:#d9dde6;
  }
  *{margin:0;padding:0;box-sizing:border-box}
  html,body{width:1200px;height:900px;overflow:hidden;background:var(--stage);font-family:"Poppins",sans-serif}
  .stage{position:relative;width:1200px;height:900px}
  .card{position:absolute;left:290px;width:620px;height:354px;background:var(--navy);overflow:hidden;box-shadow:0 10px 30px rgba(15,33,71,.25)}
  .card--back{top:48px}
  .card--front{top:498px}

  .card__panels{position:absolute;inset:0}

  .brand{position:absolute;display:flex;align-items:center;gap:14px;white-space:nowrap}
  .brand__mark{flex:0 0 auto;width:40px;height:40px;border-radius:4px;background:var(--cyan)}
  .brand__name{font-weight:500;color:var(--teal);letter-spacing:.5px;line-height:1;white-space:nowrap}

  .card--back .brand{left:70px;top:62px}
  .card--back .brand__name{font-size:40px}

  .divider{position:absolute;left:262px;right:40px;top:180px;height:2px;background:var(--lime)}

  .person{position:absolute;left:40px;top:150px}
  .person__name{font-weight:700;font-size:17px;line-height:22px;color:var(--teal);letter-spacing:.5px;text-transform:uppercase}
  .person__title{font-weight:500;font-size:13px;line-height:18px;color:var(--lime);white-space:nowrap}
  .person__company{font-size:13px;line-height:18px;color:var(--teal);margin-top:8px}
  .person__address{font-size:13px;color:var(--white);line-height:17.5px}
  .person__offices{font-size:13px;line-height:18px;color:var(--teal);margin-top:6px}
  .offices{display:flex;gap:6px;margin-top:4px}
  .offices__dot{width:22px;height:22px;border-radius:50%;background:var(--flag);border:2px solid var(--white)}

  .contact{position:absolute;right:34px;bottom:46px;text-align:right;color:var(--white);font-size:13px;line-height:1.6}
  .contact__row{display:flex;align-items:center;justify-content:flex-end;gap:8px}
  .contact__icon{width:13px;height:13px}

  .card--front .brand{left:50%;top:118px;transform:translateX(-50%)}
  .card--front .brand__mark{width:52px;height:52px}
  .card--front .brand__name{font-size:52px}

  .tagline-band{position:absolute;left:0;right:0;top:250px;height:40px;background:linear-gradient(90deg,var(--teal),var(--lime));display:flex;align-items:center;justify-content:center}
  .tagline-band__text{font-weight:500;font-size:16px;color:var(--navy);letter-spacing:.3px;white-space:nowrap}
</style>
</head>
<body>
<main class="stage">

  <section class="card card--back" aria-label="Card back with contact details">
    <svg class="card__panels" viewBox="0 0 620 354" aria-hidden="true">
      <rect x="250" y="-20" width="420" height="160" rx="22" fill="var(--navy-soft)" opacity=".7"/>
      <path d="M330 90 L560 90 Q590 90 590 120 L590 200 Q590 230 560 250 L420 330 Q395 345 380 320 Z" fill="var(--navy-panel)" opacity=".8"/>
      <rect x="-20" y="190" width="250" height="190" rx="22" fill="var(--navy-soft)" opacity=".6"/>
    </svg>

    <div class="brand">
      <span class="brand__mark"></span>
      <span class="brand__name">Veltrano Energy</span>
    </div>

    <div class="divider"></div>

    <div class="person">
      <p class="person__name">Dorian Kettle</p>
      <p class="person__title">Founder / Operations Strategist</p>
      <p class="person__company">Veltrano Energy</p>
      <p class="person__address">418 Marlow Crest Way<br>Brookhaven, FL 32000</p>
      <p class="person__offices">Offices</p>
      <div class="offices" role="img" aria-label="Office country flags: United States, United Kingdom, Canada">
        <span class="offices__dot"></span><span class="offices__dot"></span><span class="offices__dot"></span>
      </div>
    </div>

    <div class="contact">
      <p class="contact__row">555.014.2290
        <svg class="contact__icon" viewBox="0 0 24 24" aria-hidden="true"><path d="M6.6 10.8a15 15 0 0 0 6.6 6.6l2.2-2.2a1 1 0 0 1 1-.25 11 11 0 0 0 3.6.6 1 1 0 0 1 1 1V20a1 1 0 0 1-1 1A17 17 0 0 1 3 4a1 1 0 0 1 1-1h3.5a1 1 0 0 1 1 1c0 1.25.2 2.45.6 3.6a1 1 0 0 1-.25 1z" fill="var(--cyan)"/></svg>
      </p>
      <p class="contact__row">www.veltranoenergy.example
        <svg class="contact__icon" viewBox="0 0 24 24" aria-hidden="true"><g fill="none" stroke="var(--cyan)" stroke-width="2"><circle cx="12" cy="12" r="10"/><path d="M2 12h20M12 2a15 15 0 0 1 0 20M12 2a15 15 0 0 0 0 20"/></g></svg>
      </p>
    </div>
  </section>

  <section class="card card--front" aria-label="Card front with brand name and tagline">
    <div class="brand">
      <span class="brand__mark"></span>
      <span class="brand__name">Veltrano Energy</span>
    </div>
    <div class="tagline-band">
      <p class="tagline-band__text">No Debt, No Liens, No Maintenance, Just Savings.</p>
    </div>
  </section>

</main>
</body>
</html>
```